bluecastle aquatics of northeast florida business card

I need a new attractive business card. I am planning on printing on very thick rounded corner stock and having painted edges. We are a swimming pool remodel, repair, and service company in north florida. Our current logo is red, white, and blue. It doesn't necessarily have to stay that way, I am open to other ideas. It will need to contain my name, work and cell numbers, email, website, and my contractor license number.

Target Market(s)

High end residential and commercial clients

Industry/Entity Type

Business

Contact Information for Business Card

Company name, employee name and title, work and cell phone numbers, email and website, and Contractor number.

our work scope should be on card somewhere: remodel ~ repair ~ service

logo or slight variation of logo also. (not necessarily set on keeping exact logo)

Colors

Designer to choose colors to be used in the design.

Requirements
Nice to have
• We deal with water so I think some sort of water element or just a color similar to pool water would be nice to integrate into design.

```html
<!DOCTYPE html>
<html lang="en">
<head>
<meta charset="utf-8">
<title>Bluecastle Aquatics of Northeast Florida – Business Card</title>
<link href="https://fonts.googleapis.com/css2?family=Tinos:wght@400;700&display=swap" rel="stylesheet">
<style>
  :root {
    --brand-blue: #1f6fbf;
    --text-blue: #2a78c2;
    --brand-red: #e0252b;
    --card-edge: #3a3a3a;
    --water-light: #5cc8f2;
    --water-mid: #2fa8e4;
    --water-deep: #1b8fd4;
    --paper: #ffffff;
  }
  html, body {
    margin: 0;
    padding: 0;
    width: 1200px;
    height: 1000px;
    overflow: hidden;
    background: var(--paper);
    font-family: "Tinos", "Times New Roman", serif;
  }
  .canvas { position: relative; width: 1200px; height: 1000px; }
  .card {
    position: absolute;
    top: 357px;
    width: 475px;
    height: 278px;
  }
  .card--front { left: 100px; }
  .card--back { left: 642px; }
  .card__art { position: absolute; inset: 0; }
  .card__content { position: absolute; inset: 0; }
  .line { position: absolute; white-space: nowrap; margin: 0; }

  .holder-name { left: 27px; top: 42px; font-size: 19px; font-weight: 700; color: var(--brand-blue); }
  .license { left: 28px; top: 67px; font-size: 13px; color: var(--text-blue); }
  .phone { left: 27px; font-size: 14px; color: var(--brand-red); }
  .phone--work { top: 96px; }
  .phone--cell { top: 114px; }
  .phone b, .email b { font-weight: 700; }
  .email { left: 27px; top: 138px; font-size: 14px; color: var(--text-blue); }
  .website { left: 27px; top: 169px; font-size: 13px; font-weight: 700; color: var(--brand-red); }

  .company {
    position: absolute;
    left: 27px;
    top: 212px;
    margin: 0;
    color: var(--brand-blue);
    font-size: 17px;
    font-weight: 700;
    line-height: 22px;
  }
  .company span { display: block; white-space: nowrap; }

  .scope { position: absolute; left: 26px; top: 22px; margin: 0; padding: 0; list-style: none; }
  .scope__item { font-size: 30px; color: var(--text-blue); line-height: 37px; display: flex; align-items: center; }
  .scope__item::before {
    content: ""; width: 6px; height: 6px; border-radius: 50%;
    background: var(--brand-red); margin-right: 9px; margin-top: 4px;
  }
</style>
</head>
<body>
<div class="canvas">

  <section class="card card--front">
    <svg class="card__art" width="475" height="278" viewBox="0 0 475 278">
      <defs>
        <clipPath id="front-shape"><rect x="0.5" y="0.5" width="474" height="277" rx="28"/></clipPath>
        <linearGradient id="front-water" x1="0" y1="0" x2="1" y2="1">
          <stop offset="0" stop-color="var(--water-light)"/>
          <stop offset="0.55" stop-color="var(--water-mid)"/>
          <stop offset="1" stop-color="var(--water-deep)"/>
        </linearGradient>
      </defs>
      <rect x="0.5" y="0.5" width="474" height="277" rx="28" fill="var(--paper)"/>
      <g clip-path="url(#front-shape)">
        <path role="img" aria-label="Rippling swimming pool water surface"
              d="M153,0 C300,28 392,118 372,178 C362,214 348,248 334,278 L475,278 L475,0 Z"
              fill="url(#front-water)"/>
      </g>
      <rect x="0.5" y="0.5" width="474" height="277" rx="28" fill="none" stroke="var(--card-edge)" stroke-width="1"/>
    </svg>
    <div class="card__content">
      <p class="line holder-name">John Smith</p>
      <p class="line license">Contractor #12345</p>
      <p class="line phone phone--work"><b>W:</b> 940-555-0142</p>
      <p class="line phone phone--cell"><b>C:</b> 940-000-0000</p>
      <p class="line email"><b>E:</b> jsmith@bluecastlemail.com</p>
      <p class="line website">www.bluecastle-jacksonville.com</p>
      <p class="company"><span>Bluecastle Aquatics</span><span>of Northeast Florida</span></p>
    </div>
  </section>

  <section class="card card--back">
    <svg class="card__art" width="475" height="278" viewBox="0 0 475 278">
      <defs>
        <clipPath id="back-shape"><rect x="0.5" y="0.5" width="474" height="277" rx="28"/></clipPath>
        <linearGradient id="back-water" x1="0" y1="0" x2="1" y2="1">
          <stop offset="0" stop-color="var(--water-light)"/>
          <stop offset="0.55" stop-color="var(--water-mid)"/>
          <stop offset="1" stop-color="var(--water-deep)"/>
        </linearGradient>
      </defs>
      <rect x="0.5" y="0.5" width="474" height="277" rx="28" fill="var(--paper)"/>
      <g clip-path="url(#back-shape)">
        <path role="img" aria-label="Rippling swimming pool water surface"
              d="M153,0 C300,28 392,118 372,178 C362,214 348,248 334,278 L475,278 L475,0 Z"
              fill="url(#back-water)"/>
      </g>
      <rect x="0.5" y="0.5" width="474" height="277" rx="28" fill="none" stroke="var(--card-edge)" stroke-width="1"/>
    </svg>
    <div class="card__content">
      <ul class="scope">
        <li class="scope__item">Remodel</li>
        <li class="scope__item">Repair</li>
        <li class="scope__item">Service</li>
      </ul>
      <p class="company"><span>Bluecastle Aquatics</span><span>of Northeast Florida</span></p>
    </div>
  </section>

</div>
</body>
</html>
```